Business Card Design Project

KV Strategy Partners is a management consulting business with C-suite (CEO/CFO etc) target clients. Logo selected is blue with simple/serious typefaces.

Target Market(s)

CEOs and CFOs of large corporates

Industry/Entity Type

Management Consulting

Font styles to use
Serif

Colors
3276b5

Requirements
Must have
• Tag line: Creating Stronger Client Alliances (use different font)
Address: 457 Cedar Brook Lane #03-22 Singapore 519307
Telephone: +65 8372 6094
Email: kvlorne@mailbox47.com

```html
<!DOCTYPE html>
<html lang="en">
<head>
<meta charset="utf-8">
<title>KV Strategy Partners – Business Cards</title>
<link rel="stylesheet" href="https://fonts.googleapis.com/css2?family=Aleo:wght@400;700&family=Marcellus+SC&display=swap">
<style>
  :root {
    --bg: #b4b4b4;
    --frame: #333333;
    --blue: #3276b5;
    --navy: #1e3f78;
    --arrow: #17467a;
    --paper: #f3f3f3;
    --white: #ffffff;
  }
  * { margin: 0; padding: 0; box-sizing: border-box; }
  html, body { width: 1040px; height: 1200px; overflow: hidden; background: var(--bg); }
  .canvas { position: relative; width: 1040px; height: 1200px; }

  .card {
    position: absolute; left: 100px; width: 840px; height: 480px;
    background: var(--frame);
    box-shadow: 0 4px 14px rgba(0,0,0,0.35);
  }
  .card--front { top: 84px; }
  .card--back { top: 628px; }

  .band { position: absolute; left: 29px; width: 781px; overflow: hidden; }
  .band--top { top: 30px; height: 122px; background: var(--blue); }
  .band--middle { top: 163px; height: 151px; background: var(--paper); }
  .band--bottom { top: 327px; height: 122px; background: var(--blue); }

  .arrow { position: absolute; fill: var(--arrow); }

  .person { position: absolute; left: 527px; top: 58px; color: var(--white); font-family: "Aleo", serif; }
  .person__name { font-weight: 700; font-size: 29px; line-height: 32px; letter-spacing: -0.5px; }
  .person__title { font-weight: 400; font-size: 25px; line-height: 26px; }

  .brand {
    position: absolute; left: 0; right: 0; top: 34px;
    text-align: center;
    font-family: "Aleo", serif; font-weight: 700; font-size: 48px; line-height: 56px;
    color: var(--navy); letter-spacing: 0.5px;
  }
  .card--back .brand { top: 46px; }

  .tagline {
    position: absolute; left: 0; right: 0; text-align: center; white-space: nowrap;
    font-family: "Marcellus SC", serif; letter-spacing: 1.5px;
  }
  .tagline--on-paper { top: 112px; font-size: 32px; line-height: 36px; color: var(--navy); }
  .tagline--on-blue { top: 38px; font-size: 37px; line-height: 42px; color: var(--white); }

  .contact { position: absolute; left: 0; top: 12px; width: 100%; font-family: "Aleo", serif; color: var(--white); font-size: 28px; line-height: 32px; letter-spacing: 0.3px; }
  .contact__line { position: absolute; white-space: nowrap; }
</style>
</head>
<body>
<div class="canvas">

  <section class="card card--front">
    <div class="band band--top">
      <svg class="arrow" style="left:487px;top:48px" width="30" height="32" viewBox="0 0 30 32"><polygon points="0,0 30,16 0,32"/></svg>
      <svg class="arrow" style="left:501px;top:84px" width="22" height="24" viewBox="0 0 22 24"><polygon points="0,0 22,12 0,24"/></svg>
      <div class="person">
        <div class="person__name">LORNE VANCE</div>
        <div class="person__title">your title</div>
      </div>
    </div>

    <div class="band band--middle">
      <div class="brand">KV Strategy Partners</div>
      <div class="tagline tagline--on-paper">Creating Stronger Client Alliances</div>
    </div>

    <div class="band band--bottom">
      <svg class="arrow" style="left:22px;top:16px" width="30" height="32" viewBox="0 0 30 32"><polygon points="0,0 30,16 0,32"/></svg>
      <svg class="arrow" style="left:32px;top:48px" width="26" height="28" viewBox="0 0 26 28"><polygon points="0,0 26,14 0,28"/></svg>
      <svg class="arrow" style="left:22px;top:80px" width="30" height="32" viewBox="0 0 30 32"><polygon points="0,0 30,16 0,32"/></svg>
      <div class="contact">
        <div class="contact__line" style="left:57px;top:0">+65 8372 6094</div>
        <div class="contact__line" style="left:65px;top:31px">kvlorne@mailbox47.com</div>
        <div class="contact__line" style="left:65px;top:64px">457 Cedar Brook Lane #03-22 Singapore 519307</div>
      </div>
    </div>
  </section>

  <section class="card card--back">
    <div class="band band--top"></div>
    <div class="band band--middle">
      <div class="brand">KV Strategy Partners</div>
    </div>
    <div class="band band--bottom">
      <div class="tagline tagline--on-blue">Creating Stronger Client Alliances</div>
    </div>
  </section>

</div>
</body>
</html>
```